Awards Banquet Invitation

The Millbrook Valley Chamber of Commerce is celebrating it's 65th year at our Annual Awards Banquet (business leader awards). Since we were founded in 1950, we will have a 1950's theme. Dress will be 1950's Formal. I don't want cheesy 1950's. I want Classic feel and fonts from that era. This event is for business professionals so looks from ads in the 50's would be good for inspiration. I would like a look that I can use for the program and event ads. Invitation will include an RSVP insert. Date: February 10, 2015. Time: 6 cocktails, 7 dinner & program, Location: Delwen Oaks Country Club. Dress is 1950's formal

Target Market(s)

Business owners - our members

Industry/Entity Type

Business

• Lasalle, linotype, thirsty

Colors
86cfc6
474747
ffffff
000000

Requirements
Must have
• classic 50's font and old-fashioned feel
Should not have
• sock hop, soda fountain, 50's diner

```html
<!DOCTYPE html>
<html lang="en">
<head>
<meta charset="utf-8">
<title>65th Anniversary Invitation – Envelope Dieline</title>
<link rel="stylesheet" href="https://fonts.googleapis.com/css2?family=Arimo&family=Pinyon+Script&display=swap">
<style>
  :root {
    --mint: #86f8c0;
    --gold: #d39a0e;
    --gold-light: #e2ad36;
    --charcoal: #2f3336;
    --ink: #000000;
    --paper: #ffffff;
  }
  html, body {
    margin: 0;
    padding: 0;
    overflow: hidden;
    background: var(--paper);
  }
  .canvas {
    width: 1075px;
    height: 1200px;
    position: relative;
    overflow: hidden;
    background: var(--paper);
  }
  .dieline { display: block; width: 1075px; height: 1200px; }
  .mint { fill: var(--mint); }
  .gold { fill: var(--gold); }
  .charcoal { fill: var(--charcoal); }
  .ink { fill: var(--ink); }
  .script {
    font-family: "Pinyon Script", cursive;
    fill: var(--ink);
  }
  .fold-label {
    font-family: "Arimo", Arial, sans-serif;
    font-size: 26px;
    fill: var(--ink);
  }
  .fold-arrow {
    fill: none;
    stroke: var(--ink);
    stroke-width: 3.5;
    stroke-linecap: round;
  }
</style>
</head>
<body>
<main class="canvas">
  <svg class="dieline" viewBox="0 0 916 1021" preserveAspectRatio="none" xmlns="http://www.w3.org/2000/svg">
    <defs>
      <marker id="arrowhead" viewBox="0 0 10 10" refX="6" refY="5" markerWidth="5" markerHeight="5" orient="auto">
        <path d="M0,0 L10,5 L0,10 L3,5 Z" class="ink"/>
      </marker>
      <linearGradient id="floral-tone" x1="0" y1="0" x2="0" y2="1">
        <stop offset="0" stop-color="#a97b1a"/>
        <stop offset="0.5" stop-color="#c38f1c"/>
        <stop offset="1" stop-color="#a97b1a"/>
      </linearGradient>
      <clipPath id="left-panel-clip"><rect x="50" y="276" width="208" height="474"/></clipPath>
      <clipPath id="right-panel-clip"><rect x="672" y="276" width="206" height="474"/></clipPath>
    </defs>

    <!-- Top flap -->
    <path class="mint top-flap" d="M258,240 V237 A207,207 0 0 1 672,237 V240 Z"/>

    <!-- Title plaque, printed upside down on the flap -->
    <g class="title-plaque" transform="rotate(180 462 140)">
      <ellipse class="ink" cx="469" cy="147" rx="156" ry="45"/>
      <ellipse class="gold" cx="462" cy="140" rx="155" ry="44"/>
      <text class="script" x="462" y="155" font-size="50" text-anchor="middle">Invitation</text>
    </g>

    <!-- Upper bands -->
    <rect class="gold" x="50" y="232" width="828" height="22"/>
    <rect class="mint" x="50" y="254" width="828" height="22"/>

    <!-- Side panels -->
    <rect class="charcoal side-panel" x="50" y="276" width="208" height="474"/>
    <rect class="charcoal side-panel" x="672" y="276" width="206" height="474"/>

    <!-- Floral areas -->
    <rect x="62" y="282" width="208" height="458" fill="url(#floral-tone)" opacity="0.55" role="img" aria-label="Gold floral vine ornament, left panel"/>
    <rect x="660" y="282" width="206" height="458" fill="url(#floral-tone)" opacity="0.55" role="img" aria-label="Gold floral vine ornament, right panel"/>

    <!-- Centre panel with rounded shoulders -->
    <rect class="mint centre-panel" x="258" y="276" width="414" height="474"/>
    <path class="mint" d="M175,276 H258 V375 A83,83 0 0 1 175,292 Z"/>
    <path class="mint" d="M755,276 H672 V375 A83,83 0 0 0 755,292 Z"/>

    <!-- Lower corner cut-outs -->
    <g clip-path="url(#left-panel-clip)"><circle class="mint" cx="85" cy="765" r="98"/></g>
    <g clip-path="url(#right-panel-clip)"><circle class="mint" cx="845" cy="765" r="98"/></g>

    <!-- Lower bands -->
    <rect class="mint" x="50" y="750" width="828" height="22"/>
    <rect class="gold" x="50" y="772" width="828" height="21"/>

    <!-- Bottom flap -->
    <path class="mint bottom-flap" d="M258,790 V793 A207,207 0 0 0 672,793 V790 Z"/>

    <!-- Anniversary lettering, printed upside down -->
    <g class="anniversary" transform="rotate(180 465 870)">
      <text class="script" x="465" y="836" font-size="44" text-anchor="middle">65<tspan font-size="18" dy="-22">th</tspan></text>
      <text class="script" x="465" y="868" font-size="19" text-anchor="middle">Anniversary Celebration</text>
      <text class="script" x="465" y="910" font-size="22" text-anchor="middle">The Millbrook Valley Chamber of Commerce</text>
    </g>

    <!-- Folding instructions -->
    <text class="fold-label" x="131" y="90">fold 4</text>
    <path class="fold-arrow" d="M332,104 C300,70 240,95 256,163" marker-end="url(#arrowhead)"/>

    <text class="fold-label" x="53" y="180">fold 2</text>
    <path class="fold-arrow" d="M131,255 C95,225 125,190 216,208" marker-end="url(#arrowhead)"/>

    <text class="fold-label" x="717" y="182">fold 1</text>
    <path class="fold-arrow" d="M787,265 C815,245 815,200 700,213" marker-end="url(#arrowhead)"/>

    <text class="fold-label" x="98" y="890">fold 3</text>
    <path class="fold-arrow" d="M318,920 C310,975 240,950 236,872" marker-end="url(#arrowhead)"/>
  </svg>
</main>
</body>
</html>
```